KVT Building And Maintenance

Need a very professional looking double sided Buisiness card with all my details phone number, name, email, license number.

Target Market(s)

construction industry

Industry/Entity Type

building

Contact Information for Business Card

Name Dale Pemberton. Email Address Info@KVTBuilding.com.au mobile number 0452918736 licence number 671093D. web site

```html
<!DOCTYPE html>
<html lang="en">
<head>
<meta charset="UTF-8">
<title>KVT Building And Maintenance – Business Card</title>
<link href="https://fonts.googleapis.com/css2?family=Montserrat:wght@700;800&family=Open+Sans:wght@400;600&display=swap" rel="stylesheet">
<style>
  :root {
    --stage: #2b2c2e;
    --card-white: #ffffff;
    --brand-blue: #3f98d8;
    --back-blue: #4a9bd6;
    --back-blue-deep: #3f8fcb;
    --ink-dark: #3a3b3d;
    --ink-mid: #4a4b4d;
  }
  * { margin: 0; padding: 0; box-sizing: border-box; }
  html, body { width: 1200px; height: 900px; overflow: hidden; }
  body {
    background: var(--stage);
    display: flex;
    align-items: center;
    justify-content: center;
    gap: 40px;
    font-family: "Open Sans", Arial, sans-serif;
  }
  .card {
    width: 540px;
    height: 330px;
    border-radius: 18px;
    position: relative;
    overflow: hidden;
  }
  /* Front */
  .card-front {
    background: var(--card-white);
    display: flex;
    align-items: center;
    padding: 0 34px 0 40px;
  }
  .brand-block {
    width: 210px;
    display: flex;
    justify-content: center;
  }
  .brand-name {
    font-family: "Montserrat", Arial, sans-serif;
    font-weight: 800;
    font-size: 40px;
    line-height: 1.05;
    color: var(--ink-dark);
    text-transform: uppercase;
    text-align: center;
    letter-spacing: 1px;
  }
  .divider {
    width: 2px;
    height: 190px;
    background: var(--brand-blue);
    margin: 0 26px 0 16px;
  }
  .details { flex: 1; }
  .person-name {
    font-family: "Montserrat", Arial, sans-serif;
    font-weight: 700;
    font-size: 21px;
    color: var(--brand-blue);
    text-transform: uppercase;
    letter-spacing: 0.5px;
  }
  .person-role {
    font-size: 14px;
    color: var(--ink-mid);
    margin-top: 2px;
  }
  .licence {
    font-size: 14px;
    color: var(--brand-blue);
    margin-top: 6px;
    margin-bottom: 14px;
  }
  .licence .licence-number { color: var(--ink-mid); }
  .contact-list { list-style: none; }
  .contact-item {
    display: flex;
    align-items: center;
    gap: 8px;
    font-size: 14px;
    color: var(--ink-mid);
    line-height: 1.75;
  }
  .contact-item svg { width: 13px; height: 13px; flex: none; }
  .web-accent { color: var(--brand-blue); }
  /* Back */
  .card-back {
    background: linear-gradient(135deg, var(--back-blue), var(--back-blue-deep));
  }
  .back-texture {
    position: absolute;
    inset: 0;
  }
  .back-brand {
    position: absolute;
    top: 34px;
    right: 40px;
    font-family: "Montserrat", Arial, sans-serif;
    font-weight: 800;
    font-size: 24px;
    color: var(--card-white);
    letter-spacing: 1px;
  }
</style>
</head>
<body>

  <section class="card card-front" aria-label="Business card front">
    <div class="brand-block">
      <p class="brand-name">KVT<br>Building</p>
    </div>
    <div class="divider"></div>
    <div class="details">
      <h1 class="person-name">Dale Pemberton</h1>
      <p class="person-role">Director</p>
      <p class="licence">licence number <span class="licence-number">671093D.</span></p>
      <ul class="contact-list">
        <li class="contact-item">
          <svg viewBox="0 0 12 12" aria-hidden="true"><rect x="3" y="0.5" width="6" height="11" rx="1.2" fill="none" stroke="var(--brand-blue)" stroke-width="1.2"/><line x1="5" y1="9.5" x2="7" y2="9.5" stroke="var(--brand-blue)" stroke-width="1"/></svg>
          045-291-8736
        </li>
        <li class="contact-item">
          <svg viewBox="0 0 12 12" aria-hidden="true"><rect x="0.5" y="2" width="11" height="8" fill="var(--brand-blue)"/><polyline points="0.5,2 6,7 11.5,2" fill="none" stroke="#fff" stroke-width="1"/></svg>
          Info@KVTBuilding.com.au
        </li>
        <li class="contact-item">
          <svg viewBox="0 0 12 12" aria-hidden="true"><circle cx="6" cy="6" r="5.5" fill="var(--brand-blue)"/><ellipse cx="6" cy="6" rx="2.3" ry="5.5" fill="none" stroke="#fff" stroke-width="0.8"/><line x1="0.5" y1="6" x2="11.5" y2="6" stroke="#fff" stroke-width="0.8"/></svg>
          <span>www.<span class="web-accent">kvtbuilding</span>.com.au</span>
        </li>
      </ul>
    </div>
  </section>

  <section class="card card-back" aria-label="Business card back">
    <div class="back-texture" role="img" aria-label="Repeating embossed brand pattern in tonal blue"></div>
    <p class="back-brand">KVT</p>
  </section>

</body>
</html>
```